Tavner Golf Academy Brochure Design Project

We need a tri- fold brochure for our golf academy. Tavner Golf Academy was founded by Dale Tavner, a strength coach on the NLK Circuit. Our Academy fuses Swing instruction, 3D biomechanic analysis and fitness training. We would like to incorporate the colors green, grey/silver and possible black. The final design should communicate movement/action and health.
Updates
The brochure is tri fold, double sided. Front cover should include logo, and a photo of a golfer. inside should include a a history of our company, and the services we offer(I will provide). Back middle panel should be white, with logo on the top and space for address and contact info on the bottom (we currently have 2 locations, and may want to tailor this information). The other fold in should include testamonials (I will provide). Thank you.
Include the following Titles, pictures and descriptions under 'Service'
Industry/Entity Type
Fitness
Requirements
Must have
- photos of people recieving golf instruction, people performing functional exercise training (stability balls, tubing, medicine balls, stretching) We would like to designate a space to give a description of each of our services: 1)Golf Performance Evaluation. 2)Swing Coaching. 3)3D and Video Feedback Coaching. 4)Golf Performance (fitness) Coaching.
Testimonials from the Pros:
“I have trained exclusively with Dale for the last several years. Under his guidance, I have greatly enhanced my power, flexibility, and endurance on the course. As Head Strength and Conditioning Coach for the NLK, Dale personalizes cutting-edge golf fitness programs for me, so I know that every day I play, I am at the top of my game. As Dale’s fitness student and friend, I will thoroughly enjoy watching him create one of the world’s foremost golf performance companies.” - Tod Bramwell, 16 time NLK Circuit winner, Winner of the 2003 Corvane Classic, 2010 Halvery Trophy Champion
“Dale has really helped me take my golf fitness to the next level. Preventing injury, strength training, stability, flexibility, and generating power are some of the areas we have worked on and improved!” - Matías Orduna, 3 time NLK Circuit winner, 3 time Westmarch State College All American, 2 time MVC Player of the Year
“Dale Tavner is one of the most knowledgeable and enthusiastic trainers in the business. Whether it be golf specific, bust your butt or light stretching, Dale has a varied, experienced and fun way to train!”- Glen Purdey, Winner, 2005 Morton Quill Award, 8 time NLK Circuit winner, 20 professional wins
“I trust and rely on Dale to get me ready for every round of golf that I play on the NLK Circuit. He is definitely one of the best in the industry.”- Wendell Pruitt, NLK Circuit Professional Golfer, Winner, 2007 Lyle Dunmore Vantrex Invitational, 2010 Ostrava Mutual Championship
“Since I started working with Dale my endurance, flexibility and strength have improved dramatically. His golf specific program has really shored up the weak areas of my body. He has also really helped me come back from my knee and back injuries.” - Lonnie Gressett, 4 time NLK Circuit Winner

```html
<!DOCTYPE html>
<html lang="en">
<head>
<meta charset="utf-8">
<title>Tavner Golf Academy – Tri-fold Brochure</title>
<link href="https://fonts.googleapis.com/css2?family=Arimo:wght@400;700&family=Archivo+Narrow:wght@400;700&family=Marcellus&family=PT+Sans:ital@1&family=Carlito:wght@400;700&display=swap" rel="stylesheet">
<style>
  :root{
    --green-deep:#0f4b27;
    --green-head:#1e8b3d;
    --green-text:#0d5a22;
    --grey:#9b9b9c;
    --silver:#c9cbcc;
    --ink:#111;
    --white:#fff;
  }
  *{box-sizing:border-box;margin:0;padding:0}
  html,body{width:839px;height:1200px;overflow:hidden;background:var(--white)}
  .brochure{position:relative;width:839px;height:1200px;font-family:Arimo,Arial,sans-serif}
  .block{position:absolute}
  .strip{background:var(--green-deep)}
  .panel-grey{background:var(--grey)}

  /* outside spread */
  .info{left:52px;top:0;width:207px;color:var(--ink);font-size:9.4px;line-height:11px;text-align:justify}
  .info h3{color:var(--green-text);font-weight:400;font-size:9.4px;line-height:11px}
  .info .driving{position:absolute;top:35px;left:0;width:207px}
  .info .lessons{position:absolute;top:180px;left:0;width:207px}
  .info .events{position:absolute;top:358px;left:0;width:207px}
  .info p + p{margin-top:11px}

  .mail-band{left:282px;top:0;width:275px;height:48px;background:linear-gradient(#e4e5e6,var(--silver) 60%,#a9abac);border-radius:0 0 6px 6px;display:flex;align-items:center;justify-content:center}
  .mail-band .name{background:var(--green-deep);color:var(--white);font-family:Carlito,sans-serif;font-weight:700;font-size:11px;letter-spacing:1px;padding:5px 14px;border-radius:0 0 10px 10px}
  .contact{left:280px;width:279px;text-align:center;font-family:Carlito,sans-serif;font-size:10.4px;line-height:12px;color:var(--green-text)}
  .contact strong{color:var(--ink)}

  .cover-logo{left:559px;top:0;width:280px;height:63px;display:flex;align-items:center;gap:10px;padding-left:10px}
  .cover-logo .dot{width:40px;height:40px;border-radius:50%;background:var(--green-head);flex:none}
  .cover-logo .name{font-family:Arimo,sans-serif;font-weight:700;font-size:21px;color:var(--green-head);line-height:22px}
  .cover-photo{left:559px;top:63px;width:280px;height:507px;background:linear-gradient(180deg,#9fb4a8 0%,#c7d0bf 30%,#7f9a64 55%,#3e6a2a 80%,#2f5520 100%)}
  .cover-photo svg{position:absolute;left:0;bottom:0}

  /* inside spread */
  .heading{font-family:Marcellus,serif;color:var(--green-head);font-size:16px;font-weight:400;text-align:center;letter-spacing:.5px}
  .history{left:59px;top:685px;width:216px;color:var(--white);font-size:9.6px;line-height:11.6px;text-align:justify}
  .history p + p{margin-top:11px}

  .photo{position:absolute}
  .svc{position:absolute;font-family:"Archivo Narrow",sans-serif;font-size:9px;line-height:10.4px;color:var(--ink)}
  .svc h4{font-family:Arimo,sans-serif;font-weight:700;font-size:9.3px;line-height:11px;color:inherit}
  .svc.on-dark{color:var(--white)}
  .swing-box{left:287px;top:880px;width:263px;height:140px;background:#000}

  .quote{position:absolute;left:566px;width:230px;font-family:"PT Sans",sans-serif;font-style:italic;font-size:8.4px;line-height:10px;color:var(--ink)}
  .quote .pic{display:block}
  .quote .pic.left{float:left;margin:3px 7px 2px 0}
  .quote .pic.right{float:right;margin:3px 0 2px 6px}
  .pic{border:2px solid var(--white)}
</style>
</head>
<body>
<div class="brochure">

  <!-- Outside spread -->
  <div class="block strip" style="left:0;top:0;width:35px;height:570px"></div>
  <div class="block panel-grey" style="left:35px;top:0;width:245px;height:570px"></div>

  <div class="block info">
    <section class="driving">
      <h3>Driving Range</h3>
      <p>Get warmed up at our driving range, fully equipped with 60 bays (20 heated) and yard markers up to 300 yards. You'll love practicing with our AutoPeg® system, automatically teeing up your ball with every shot you make. AutoPeg enables you to choose from four separate tee heights and provides a platform for timing and muscle memory that is unrivaled. We offer bucket sizes ranging from 60-140 balls, as well as discount packs for customers who wish to pre-pay.</p>
    </section>
    <section class="lessons">
      <h3>Golf Instructions</h3>
      <p>Learn from the best with golf lessons taught by NLK™ Teaching Professionals. At Tavner Golf Academy, with our seasoned instructors, you can work on every aspect of your game in our outdoor bays, on our par-3 golf course or indoors using one of our netted bays. Our instructors will work on every aspect of your swing to learning proper golf etiquette. Enroll in one of our golf schools/semi-private lessons, and you'll learn the basics of playing golf, or opt for our private lessons which are available in half-hour and one-hour sessions. Be sure to ask about our indoor golf instruction lessons and packages</p>
    </section>
    <section class="events">
      <h3>Parties &amp; Special Events</h3>
      <p>Plan your birthday party with us, allowing your friends and family to participate in any of our golf course facilities, including miniature golf.</p>
      <p>***Reserve a picnic area for your guests, with catering and refreshments provided upon request. Our facility also makes a unique destination for school events and corporate parties.</p>
    </section>
  </div>

  <div class="block mail-band"><span class="name">TAVNER GOLF ACADEMY</span></div>

  <div class="block contact" style="top:385px">
    <strong>Tavner Golf Academy</strong><br>
    123 Larkfield Street<br>
    Dunmore Ridge, NJ 12345<br>
    XXX.XXX.XXXX<br>
    www.tavnergolfacademy.com
  </div>
  <div class="block contact" style="top:458px">
    <strong>Tavner Golf Academy</strong><br>
    48 County Road 7<br>
    Dunmore Ridge, NJ 07100-2200<br>
    555.014.0272<br>
    www.tavnergolfacademy.com
  </div>

  <div class="block cover-logo">
    <span class="dot"></span>
    <span class="name">Tavner Golf Academy</span>
  </div>
  <div class="block cover-photo" role="img" aria-label="Golfer finishing a swing on a misty fairway, with faded golfers in the sky">
    <svg width="280" height="30" viewBox="0 0 280 30" aria-hidden="true">
      <path d="M0 14 C70 2 150 30 280 8 L280 30 L0 30 Z" fill="#9b9b9c"/>
    </svg>
  </div>

  <!-- Inside spread -->
  <div class="block strip" style="left:0;top:629px;width:35px;height:571px"></div>
  <div class="block panel-grey" style="left:35px;top:629px;width:245px;height:571px"></div>
  <div class="block panel-grey" style="left:559px;top:629px;width:245px;height:571px"></div>
  <div class="block strip" style="left:804px;top:629px;width:35px;height:571px"></div>

  <h2 class="block heading" style="left:35px;top:655px;width:245px">Our History</h2>
  <div class="block history">
    <p>How and where the history of golf originated is for the most part unknown and continues to be the subject of much debate. Although, for the most part it is widely understood that the Scots during the middle ages where largely responsible for creating the game of golf we play today, a claim that has undergone substantial scrutiny and numerous challenges over many centuries.</p>
    <p>There are several forerunners to the history of golf dating back as far as early 1297 to the Netherlands, leaving the Dutch to appear to have the closest ties to the origin of golf. Further evidence is supported by early 13th Century Dutch literature which contained numerous references to "golf like" games with medieval names such as "spel mitten colve" (play with club). Additionally, Dutch master painters of the day created numerous paintings and sketches of early participants playing a game with a club and ball in Holland, most certainly resembling what we know today as golf.</p>
    <p>Commerce between Scotland and Holland blossomed throughout the North Sea trade route during the beginning of the middle ages. Sailors and traders often became stranded or delayed due to bad weather and became perfect candidates to become introduced to a new and better way to enjoy their leisure time and began to participate in the favorite local sports of the day. In many instances, some of the players shown in Dutch pictures wore kilts giving a clear indication they were Scottish visitors.</p>
  </div>

  <h2 class="block heading" style="left:280px;top:655px;width:279px">Services</h2>

  <!-- 1. Evaluation -->
  <div class="svc" style="left:296px;top:688px;width:148px">
    <h4>PERFORMANCE EVALUATION:</h4>
    Our Golf Performance Evaluation screens your mobility, stability, strength and swing to find what limits your game, giving a clear starting point for every program we build
  </div>
  <div class="photo" style="left:452px;top:688px;width:98px;height:78px;background:linear-gradient(160deg,#e6ebe8,#b5c2bd 55%,#4a8a5c)" role="img" aria-label="Trainer assessing a golfer's mobility on a mat"></div>

  <!-- 2. Fitness coaching -->
  <div class="photo" style="left:296px;top:778px;width:104px;height:90px;background:linear-gradient(160deg,#e8ece9,#b9c3c0 55%,#3c8a55 80%,#2a4a8a)" role="img" aria-label="Client balancing on a stability ball with a trainer in a bright studio"></div>
  <div class="svc" style="left:410px;top:779px;width:142px">
    <h4>PERFORMANCE TRAINING:</h4>
    Performance Training focuses on improving specific mobility, stability and core strength that allow golfer's to feel and play their best. Other exercises strategies are also employed to produce efficient, powerful and durable golfers
  </div>

  <!-- 3. Swing coaching -->
  <div class="block swing-box"></div>
  <div class="photo" style="left:296px;top:889px;width:100px;height:122px;background:linear-gradient(180deg,#e9eef2 0%,#cfd9df 45%,#6d8a5a 70%,#3f5f32 100%)" role="img" aria-label="Golfer swinging on an outdoor course"></div>
  <div class="svc on-dark" style="left:408px;top:888px;width:136px">
    <h4>SWING COACHING:</h4>
    Swing Coaching focuses on teaching the fundamentals of the golf swing from the set-up, grip, aim, alignment, and club path
  </div>
  <div class="photo" style="left:420px;top:940px;width:118px;height:71px;background:linear-gradient(180deg,#b9c7cf 0%,#6f8f9a 40%,#4d7a3a 70%,#2d4d22 100%)" role="img" aria-label="Coach adjusting a student's grip and setup"></div>

  <!-- 4. 3D and video feedback -->
  <div class="svc" style="left:287px;top:1034px;width:92px">
    <h4>3D &amp; VIDEO FEEDBACK:</h4>
    Our 3D Biomechanics and video training focuses on developing an efficient golf swing via the kinematic sequence. Effortless power and a safe, efficient and reproducible swing are developed
  </div>
  <div class="photo" style="left:384px;top:1034px;width:166px;height:120px;background:linear-gradient(90deg,#111 0%,#2d2d2d 45%,#dfe3e1 55%,#7ccf5a 80%,#e6e8e7 100%)" role="img" aria-label="Golfer with motion sensors beside 3D swing analysis screen"></div>

  <h2 class="block heading" style="left:559px;top:655px;width:245px">Testimonials</h2>

  <div class="quote" style="top:677px">
    <span class="pic left" style="width:68px;height:77px;background:linear-gradient(180deg,#d7e0d0,#7f9b6e 70%,#3e5a2e)" role="img" aria-label="Tod Bramwell at the end of a swing"></span>
    “I have trained exclusively with Dale for the last several years. Under his guidance, I have greatly enhanced my power, flexibility, and endurance on the course. As Head Strength and Conditioning Coach for the NLK, Dale personalizes cutting-edge golf fitness programs for me, so I know that every day I play, I am at the top of my game. As Dale’s fitness student and friend, I will thoroughly enjoy watching him create one of the world’s foremost golf performance companies.” - Tod Bramwell, 16 time NLK Circuit winner, Winner of the 2003 Corvane Classic, 2010 Halvery Trophy Champion
  </div>

  <div class="quote" style="top:817px">
    <span class="pic right" style="width:84px;height:63px;background:linear-gradient(180deg,#3c5a2e,#6f8d4f 60%,#2c3f22)" role="img" aria-label="Matías Orduna crouching on a green"></span>
    “Dale has really helped me take my golf fitness to the next level. Preventing injury, strength training, stability, flexibility, and generating power are some of the areas we have worked on and improved!” - Matías Orduna, 3 time NLK Circuit winner, 3 time Westmarch State College All American, 2 time MVC Player of the Year
  </div>

  <div class="quote" style="top:921px">
    <span class="pic left" style="width:58px;height:66px;background:linear-gradient(180deg,#9fb3c4,#5d7f9a 55%,#3f6a35)" role="img" aria-label="Glen Purdey reading a putt"></span>
    “Dale Tavner is one of the most knowledgeable and enthusiastic trainers in the business. Whether it be golf specific, bust your butt or light stretching, Dale has a varied, experienced and fun way to train!” - Glen Purdey, Winner, 2005 Morton Quill Award, 8 time NLK Circuit winner and 20 professional wins.
  </div>

  <div class="quote" style="top:1018px">
    <span class="pic right" style="width:60px;height:70px;background:linear-gradient(180deg,#c4ccd3,#6f7d8a 55%,#2a2f36)" role="img" aria-label="Wendell Pruitt holding a trophy"></span>
    “I trust and rely on Dale to get me ready for every round of golf that I play on the NLK Circuit. He is definitely one of the best in the industry.”- Wendell Pruitt, NLK Circuit Professional Golfer, Winner, 2007 Lyle Dunmore Vantrex Invitational, 2010 Ostrava Mutual Championship
  </div>

  <div class="quote" style="top:1104px">
    <span class="pic left" style="width:67px;height:69px;background:linear-gradient(180deg,#dfe4e1,#8aa07c 60%,#3d5b31)" role="img" aria-label="Lonnie Gressett on the course"></span>
    “Since I started working with Dale my endurance, flexibility and strength have improved dramatically. His golf specific program has really shored up the weak areas of my body. He has also really helped me come back from my knee and back injuries.” - Lonnie Gressett, 4 time NLK Circuit Winner
  </div>

</div>
</body>
</html>
```